I would like a single page website for Skylark Rentals Australia. In the file list provided there is basic information to be included as well as our logo with colors, fonts and images to be included.
Site must be very simple and be able to be loaded onto smart phones etc very quickly.
Site needs to be very smart in appearance

Target Market(s)

All prospective drone customers from Police to Parties.

Industry/Entity Type

Hire

Coding

Coded - Design and coding required

Number of Pages Required

1 page

Requirements
Must have
• Must have variation of color schemes supplied
Nice to have
• Must be very eye catching without going over the top
Should not have
• Anything slow to load.

```html
<!DOCTYPE html>
<html lang="en">
<head>
<meta charset="utf-8">
<title>Skylark Rentals Australia</title>
<link href="https://fonts.googleapis.com/css2?family=Raleway:wght@400;500;700&display=swap" rel="stylesheet">
<style>
:root{
  --green:#6cb33f;
  --blue:#3a9ad9;
  --ink:#222;
  --muted:#9a9a9a;
  --body:#555;
  --band:#ededed;
  --rule:#e4e4e4;
  --white:#fff;
}
*{margin:0;padding:0;box-sizing:border-box}
html,body{width:1200px;height:1000px;overflow:hidden;background:var(--white);font-family:"Raleway",sans-serif;color:var(--ink)}
.page{position:relative;width:1200px;height:1000px}
.abs{position:absolute}

.site-header{left:336px;top:0;width:504px;height:42px;border-top:1px solid #888}
.brand{left:13px;top:12px;font-size:10px;font-weight:700;color:var(--green);line-height:10px;width:90px;letter-spacing:.3px}
.nav{right:18px;top:17px;display:flex;gap:12px;font-size:6.5px;color:#444}
.nav .active{position:relative}
.nav .active::before{content:"";position:absolute;left:-3px;right:-3px;top:-17px;height:2px;background:var(--blue)}

.hero{left:336px;top:42px;width:504px;height:234px;background:radial-gradient(ellipse at 25% 60%,#4a8a4a 0%,#2d3a2d 30%,#1e1f1a 60%,#2e2d22 100%)}
.hero-photo{left:0;top:20px;width:240px;height:190px;background:radial-gradient(ellipse at center,#d8d8d4 0%,rgba(200,200,196,.35) 45%,rgba(0,0,0,0) 70%)}
.hero-copy{left:258px;top:76px;width:210px;color:var(--white)}
.hero-copy h1{font-size:14.5px;font-weight:700;line-height:15px;margin-bottom:6px}
.hero-copy li{list-style:none;font-size:6.3px;line-height:10.8px}
.btn{display:inline-block;margin-top:8px;background:var(--white);color:#333;font-size:6.3px;padding:3px 5px}
.arrow{width:18px;height:22px;top:107px;background:rgba(0,0,0,.5);border-radius:11px}
.arrow.prev{left:-4px}.arrow.next{right:-8px}
.progress{left:0;bottom:0;width:288px;height:2px;background:var(--blue)}

.services-title{left:336px;top:326px;width:504px;text-align:center;font-size:13px;font-weight:700}
.rule{height:1px;background:var(--rule)}
.service{width:120px;text-align:center;font-size:7.5px;line-height:8px;color:var(--muted);top:357px}
.service svg{display:block;margin:0 auto 4px}

.feature-band{left:336px;top:447px;width:504px;height:161px;background:var(--band)}
.feature-band h2{position:absolute;left:13px;top:38px;width:180px;font-size:12.5px;font-weight:700;line-height:14px}
.feature-band p{position:absolute;left:13px;top:72px;width:192px;font-size:9px;line-height:12.3px;color:var(--body)}
.band-photo{left:296px;top:22px;width:200px;height:112px;background:radial-gradient(ellipse at center,#f4f4f2 0%,#e0e0dc 50%,var(--band) 75%)}

.drone-photo{left:360px;top:676px;width:208px;height:120px;background:radial-gradient(ellipse at center,#e6e6e2 0%,#f2f2f0 55%,#fff 75%)}
.checks{left:594px;top:684px;list-style:none}
.checks li{display:flex;align-items:flex-start;height:36px}
.tick{width:27px;height:27px;border:1px solid #ddd;border-radius:2px;display:flex;align-items:center;justify-content:center;margin-right:12px}
.checks strong{display:block;font-weight:400;font-size:8px;color:var(--muted);margin-top:-1px}
.checks span{display:block;font-size:6px;color:#444;margin-top:3px}

.map{left:349px;top:906px;width:314px;height:62px;background:linear-gradient(100deg,#e8e4dc 0%,#ebe7df 55%,#a8c8f0 75%,#9cc0ee 100%)}
.contact{left:676px;top:913px;font-size:6px;line-height:8.2px;color:#444}
.contact h3{font-size:11px;font-weight:700;color:var(--ink);line-height:12px;margin-bottom:4px}
.contact b{color:var(--ink)}
.footer-links{left:349px;top:972px;font-size:6px;color:var(--blue);display:flex;gap:6px}
.footer-links i{font-style:normal;color:#aaa}
.copyright{left:349px;top:988px;font-size:6px;color:#444}
</style>
</head>
<body>
<div class="page">

  <header class="site-header abs">
    <div class="brand abs">Skylark Rentals Australia</div>
    <nav class="nav abs"><span class="active">Home</span><span>Services</span><span>About</span><span>Contact</span></nav>
  </header>

  <section class="hero abs">
    <div class="hero-photo abs" role="img" aria-label="White camera drone hovering with blurred green background"></div>
    <div class="arrow prev abs"></div>
    <div class="arrow next abs"></div>
    <div class="hero-copy abs">
      <h1>4K VIDEO FOOTAGE, 12MP IMAGES</h1>
      <ul>
        <li>Construction project updates for remote stake holders</li>
        <li>Building/Roof Condition Inspections</li>
        <li>Lost pets</li>
        <li>Accident reconstructions</li>
        <li>Insurance assessing</li>
      </ul>
      <span class="btn">Read More</span>
    </div>
    <div class="progress abs"></div>
  </section>

  <h2 class="services-title abs">Our Services</h2>
  <div class="rule abs" style="left:349px;top:349px;width:479px"></div>

  <div class="service abs" style="left:344px">
    <svg width="24" height="24" viewBox="0 0 24 24" fill="#6cb33f"><rect x="2" y="13" width="20" height="10"/><rect x="4" y="8" width="2" height="5"/><rect x="11" y="8" width="2" height="5"/><rect x="18" y="8" width="2" height="5"/><circle cx="5" cy="5" r="1.5"/><circle cx="12" cy="5" r="1.5"/><circle cx="19" cy="5" r="1.5"/></svg>
    Special Occasions, Children's Birthday Parties, Weddings
  </div>
  <div class="service abs" style="left:467px">
    <svg width="24" height="24" viewBox="0 0 24 24" fill="#6cb33f"><path d="M6 2h12v6a6 6 0 0 1-12 0z"/><path d="M2 3h4v2H4a3 3 0 0 0 2 3v2a5 5 0 0 1-4-5zM22 3h-4v2h2a3 3 0 0 1-2 3v2a5 5 0 0 0 4-5z"/><rect x="11" y="13" width="2" height="5"/><rect x="7" y="19" width="10" height="3"/></svg>
    Sporting events - 4K, Video of yourself participating in marathons etc
  </div>
  <div class="service abs" style="left:588px">
    <svg width="24" height="24" viewBox="0 0 24 24" fill="#6cb33f"><path d="M12 1 1 7h22z"/><rect x="2" y="8" width="20" height="2"/><rect x="4" y="11" width="2" height="8"/><rect x="9" y="11" width="2" height="8"/><rect x="13" y="11" width="2" height="8"/><rect x="18" y="11" width="2" height="8"/><rect x="1" y="20" width="22" height="3"/></svg>
    Real Estate Brochures
  </div>
  <div class="service abs" style="left:707px">
    <svg width="24" height="24" viewBox="0 0 24 24" fill="#6cb33f"><rect x="3" y="2" width="6" height="5"/><rect x="15" y="2" width="6" height="5"/><path d="M2 8h9v14H2zM13 8h9v14h-9z"/><rect x="10" y="10" width="4" height="5"/></svg>
    Surveillance – Police, Local councils worksafe etc
  </div>

  <section class="feature-band abs">
    <div class="rule abs" style="left:13px;top:31px;width:192px"></div>
    <h2>4K Video Footage, 12mp Images</h2>
    <p>CASA certified company and CASA endorsed pilot, with Full Public Liability Insurance. All operating licences are in place and are carried on the operator. All drones are maintained to full CASA compliance standards</p>
    <div class="band-photo abs" role="img" aria-label="White quadcopter drone in flight"></div>
  </section>

  <div class="drone-photo abs" role="img" aria-label="White quadcopter drone with gimbal camera"></div>

  <ul class="checks abs">
    <li><div class="tick"><svg width="10" height="8" viewBox="0 0 10 8"><path d="M1 4l3 3 5-6" stroke="#6cb33f" stroke-width="2" fill="none"/></svg></div><div><strong>Construction project updates</strong><span>for remote stake holders</span></div></li>
    <li><div class="tick"><svg width="10" height="8" viewBox="0 0 10 8"><path d="M1 4l3 3 5-6" stroke="#6cb33f" stroke-width="2" fill="none"/></svg></div><div><strong>Building/Roof</strong><span>Condition Inspections</span></div></li>
    <li><div class="tick"><svg width="10" height="8" viewBox="0 0 10 8"><path d="M1 4l3 3 5-6" stroke="#6cb33f" stroke-width="2" fill="none"/></svg></div><div><strong>Lost</strong><span>pets</span></div></li>
    <li><div class="tick"><svg width="10" height="8" viewBox="0 0 10 8"><path d="M1 4l3 3 5-6" stroke="#6cb33f" stroke-width="2" fill="none"/></svg></div><div><strong>Accident</strong><span>reconstructions</span></div></li>
    <li><div class="tick"><svg width="10" height="8" viewBox="0 0 10 8"><path d="M1 4l3 3 5-6" stroke="#6cb33f" stroke-width="2" fill="none"/></svg></div><div><strong>Insurance</strong><span>assessing</span></div></li>
  </ul>

  <div class="map abs" role="img" aria-label="Street map showing the business location"></div>
  <div class="contact abs">
    <h3>Contact Info</h3>
    <b>Sam Harlow</b><br>
    sam@skylarkrentals.example<br>
    www.skylarkrentals.example<br>
    P: 0400 123 456
  </div>

  <div class="footer-links abs"><span>Home</span><i>·</i><span>About</span><i>·</i><span>Services</span><i>·</i><span>Contact</span></div>
  <div class="copyright abs">Copyright © Skylark Rentals Australia 2015. All Rights Reserved</div>

</div>
</body>
</html>
```